jpg 'poster' for music show to use on social media (only 72dpi needed)

style wanted: Milo Grent goes western

text:

Ray Dunkel
Anna Prescot
Neil Tomasek
Maribeth Oskarsen
... and friends

Friday April 25
Tinbarrel Coffee
Seattle

7:00 PM

$5

would love to get ASAP.

committed to pay for a cool poster!
just need 72 dpi. Thx!

not crazy particular. a cool Milo Grent type layout will be accepted :)

```html
<!DOCTYPE html>
<html lang="en">
<head>
<meta charset="utf-8">
<title>Ray Dunkel and friends — Tinbarrel Coffee, Seattle</title>
<link rel="stylesheet" href="https://fonts.googleapis.com/css2?family=Special+Elite&display=swap">
<style>
  :root {
    --page-bg: #a6dcf5;
    --poster-yellow: #e8c24a;
    --poster-glow: #f8eed4;
    --band-dark: #2a2411;
    --band-brown: #6b5234;
    --ink: #1e1a0c;
    --paper: #fffcf4;
    --price-box: #2a2513;
    --white: #ffffff;
  }
  * { margin: 0; padding: 0; box-sizing: border-box; }
  html, body { width: 1200px; height: 1000px; overflow: hidden; }
  body {
    background: var(--page-bg);
    font-family: "Special Elite", "Courier New", monospace;
  }
  .poster {
    position: absolute;
    left: 361px;
    top: 165px;
    width: 478px;
    height: 670px;
    border: 1px solid var(--ink);
    background: radial-gradient(ellipse 260px 300px at 240px 350px, var(--poster-glow) 0%, var(--poster-yellow) 100%);
    overflow: hidden;
    color: var(--ink);
  }
  .bands { position: absolute; left: 0; top: 0; width: 478px; height: 300px; }
  .band-name {
    position: absolute;
    color: var(--white);
    font-size: 26px;
    white-space: nowrap;
    letter-spacing: 1px;
    transform-origin: left center;
  }
  .band-name--first  { left: 58px;  top: 62px;  transform: rotate(-8deg); }
  .band-name--second { left: 192px; top: 98px;  transform: rotate(6deg); }
  .band-name--third  { left: 58px;  top: 162px; transform: rotate(-5deg); }
  .band-name--fourth { right: 40px; top: 231px; }
  .and-friends {
    position: absolute;
    left: 0; width: 100%;
    top: 286px;
    text-align: center;
    font-size: 26px;
    font-weight: bold;
  }
  .details-ribbon {
    position: absolute;
    left: 62px;
    top: 395px;
    width: 343px;
    height: 118px;
    background: linear-gradient(90deg, var(--poster-yellow) 0%, var(--poster-glow) 50%, var(--poster-yellow) 100%);
    box-shadow: 0 4px 8px rgba(0,0,0,0.3);
    text-align: center;
    font-size: 27px;
    line-height: 36px;
    padding-top: 4px;
  }
  .ribbon-tab {
    position: absolute;
    width: 45px;
    background: var(--paper);
    box-shadow: 0 2px 6px rgba(0,0,0,0.2);
  }
  .ribbon-tab--left  { left: 16px;  top: 385px; height: 135px; }
  .ribbon-tab--right { left: 404px; top: 385px; height: 141px; }
  .show-time {
    position: absolute;
    left: 59px;
    top: 554px;
    font-size: 24px;
  }
  .price-box {
    position: absolute;
    left: 332px;
    top: 550px;
    width: 84px;
    height: 120px;
    background: var(--price-box);
    border: 1px solid var(--ink);
  }
  .price {
    position: absolute;
    left: 0; width: 100%;
    top: 16px;
    text-align: center;
    color: var(--white);
    font-size: 40px;
    text-shadow: 0 0 8px rgba(255,210,140,0.8);
  }
</style>
</head>
<body>
  <main class="poster">
    <svg class="bands" viewBox="0 0 478 300" aria-hidden="true">
      <defs>
        <linearGradient id="band-fill" x1="0" x2="1" y1="0" y2="0">
          <stop offset="0" stop-color="var(--band-dark)"/>
          <stop offset="0.55" stop-color="var(--band-brown)"/>
          <stop offset="1" stop-color="var(--band-dark)"/>
        </linearGradient>
        <filter id="band-shadow" x="-5%" y="-20%" width="110%" height="140%">
          <feDropShadow dx="0" dy="3" stdDeviation="3" flood-opacity="0.45"/>
        </filter>
      </defs>
      <polygon class="band band--second" points="0,65 478,118 478,162 0,120" fill="url(#band-fill)" stroke="#111" filter="url(#band-shadow)"/>
      <polygon class="band band--third" points="0,170 478,125 478,162 0,214" fill="url(#band-fill)" stroke="#111" filter="url(#band-shadow)"/>
      <polygon class="band band--first" points="0,64 478,0 478,47 0,120" fill="url(#band-fill)" stroke="#111" filter="url(#band-shadow)"/>
      <rect class="band band--fourth" x="0" y="227" width="478" height="43" fill="url(#band-fill)" stroke="#111" filter="url(#band-shadow)"/>
    </svg>

    <div class="band-name band-name--first">Ray Dunkel</div>
    <div class="band-name band-name--second">Anna Prescot</div>
    <div class="band-name band-name--third">Neil Tomasek</div>
    <div class="band-name band-name--fourth">Maribeth Oskarsen</div>

    <p class="and-friends">... and friends</p>

    <div class="ribbon-tab ribbon-tab--left"></div>
    <div class="details-ribbon">
      <div class="show-date">Friday April 25</div>
      <div class="venue">Tinbarrel Coffee</div>
      <div class="city">Seattle</div>
    </div>
    <div class="ribbon-tab ribbon-tab--right"></div>

    <p class="show-time">7:00 PM</p>
    <div class="price-box"><span class="price">$5</span></div>
  </main>
</body>
</html>
```